SaaS Early tech startup business card design

Unique design for experience ecommerce platform company. the business cards will be used by executive members. conformance with color code is required.

```html
<!DOCTYPE html>
<html lang="en">
<head>
<meta charset="utf-8">
<title>kivo — business card</title>
<link rel="stylesheet" href="https://fonts.googleapis.com/css2?family=Oswald:wght@500;600&family=Roboto:wght@300;400&display=swap">
<style>
  :root {
    --backdrop: #3a3b3c;
    --paper: #ffffff;
    --navy: #0b5f8a;
    --ocean: #0a6d94;
    --steel: #168ea8;
    --teal: #0aa595;
    --sea: #14b89e;
    --mint: #2ee0bf;
    --aqua-top: #05c0b0;
    --deep-bottom: #065f8a;
    --ink: #4a4a4a;
    --mark-dark: #0a2f45;
  }
  * { margin: 0; padding: 0; box-sizing: border-box; }
  html, body { width: 1200px; height: 1200px; overflow: hidden; }
  body {
    background: var(--backdrop);
    position: relative;
    font-family: "Roboto", Arial, sans-serif;
  }
  .card {
    position: absolute;
    left: 262px;
    width: 686px;
    height: 392px;
    overflow: hidden;
  }
  .card--front { top: 165px; background: var(--paper); }
  .card--back {
    top: 653px;
    background: linear-gradient(180deg, var(--aqua-top) 0%, #05a3a2 40%, #077f98 75%, var(--deep-bottom) 100%);
  }
  .wordmark {
    position: absolute;
    font-family: "Oswald", Arial, sans-serif;
    font-weight: 600;
    letter-spacing: 2px;
    line-height: 1;
    text-transform: lowercase;
  }
  .card--front .wordmark {
    left: 82px;
    top: 140px;
    font-size: 104px;
    color: var(--ocean);
  }
  .card--back .wordmark {
    left: 0;
    right: 0;
    top: 100px;
    text-align: center;
    font-size: 170px;
    color: var(--mark-dark);
  }
  .identity { position: absolute; left: 372px; top: 80px; }
  .identity__name {
    font-family: "Oswald", Arial, sans-serif;
    font-weight: 500;
    font-size: 28px;
    line-height: 32px;
    color: var(--navy);
    text-transform: uppercase;
    letter-spacing: 0.2px;
  }
  .identity__role {
    font-weight: 300;
    font-size: 17px;
    line-height: 20px;
    color: var(--sea);
  }
  .contact { position: absolute; left: 373px; }
  .contact__icon {
    position: absolute;
    left: 0;
    width: 27px;
    height: 27px;
  }
  .contact__lines {
    position: absolute;
    left: 38px;
    top: -6px;
    font-weight: 300;
    font-size: 17px;
    line-height: 19px;
    color: var(--ink);
    white-space: nowrap;
  }
  .contact--address { top: 155px; }
  .contact--phone { top: 218px; }
  .contact--mail { top: 276px; }
  .colour-band {
    position: absolute;
    left: 0; right: 0; bottom: 0;
    height: 14px;
    display: flex;
  }
  .colour-band span { flex: 1; }
</style>
</head>
<body>
  <section class="card card--front">
    <div class="wordmark">kivo</div>

    <div class="identity">
      <div class="identity__name">Daniel Hart</div>
      <div class="identity__role">President</div>
    </div>

    <div class="contact contact--address">
      <svg class="contact__icon" viewBox="0 0 27 27" aria-hidden="true">
        <rect width="27" height="27" fill="var(--navy)"/>
        <path d="M13.5 6.5a5 5 0 0 0-5 5c0 3.6 5 9 5 9s5-5.4 5-9a5 5 0 0 0-5-5z" fill="#fff"/>
        <circle cx="13.5" cy="11.5" r="2" fill="var(--navy)"/>
      </svg>
      <div class="contact__lines">4120 Cedar Hollow Road<br>Fairbanks, Alaska 99701</div>
    </div>

    <div class="contact contact--phone">
      <svg class="contact__icon" viewBox="0 0 27 27" aria-hidden="true">
        <rect width="27" height="27" fill="var(--ocean)"/>
        <path d="M9.6 7.5l2 0 1 3-1.4 1.2c.7 1.6 1.9 2.8 3.5 3.5l1.2-1.4 3 1v2c0 .8-.7 1.4-1.5 1.3C12 17.6 9.4 15 8.9 9c-.1-.8.5-1.5 1.3-1.5z" fill="#fff"/>
      </svg>
      <div class="contact__lines">555-214-7730<br>555-318-4062</div>
    </div>

    <div class="contact contact--mail">
      <svg class="contact__icon" viewBox="0 0 27 27" aria-hidden="true">
        <rect width="27" height="27" fill="var(--teal)"/>
        <rect x="8" y="10" width="11" height="8" fill="none" stroke="#fff" stroke-width="1.3"/>
        <path d="M8 10l5.5 4.5L19 10" fill="none" stroke="#fff" stroke-width="1.3"/>
      </svg>
      <div class="contact__lines">hello@kivo.com<br>www.kivo.com</div>
    </div>

    <div class="colour-band">
      <span style="background: var(--navy)"></span>
      <span style="background: var(--ocean)"></span>
      <span style="background: var(--steel)"></span>
      <span style="background: var(--teal)"></span>
      <span style="background: var(--sea)"></span>
      <span style="background: var(--mint)"></span>
    </div>
  </section>

  <section class="card card--back">
    <div class="wordmark">kivo</div>
  </section>
</body>
</html>
```